Pebble & Co: retail package

We need packaging for kids underwear and like the concept of a drawer box with a clear cut out on top.
The package needs to have our brand name and tag line on the outer sleeve (on top) and on the back have text with our story and size chart/care instructions with logo(bottom) etc. It is preferred that the outer sleeve would in white. The inner sleeve would be a solid turq with a ribbon pull out. The design needs to be simple - to be consistent with brand image.
The dimensions would be 20cm x 15 cm x5cm
Please also check our website - Pebbleandco.com to get more info about our product line.
Target Market(s)
Mothers in the US: 20-40 years
Industry/Entity Type
Retail
Look and feel

```html
<!DOCTYPE html>
<html lang="en">
<head>
<meta charset="utf-8">
<title>Pebble & Co – Package Back Panel</title>
<link rel="stylesheet" href="https://fonts.googleapis.com/css2?family=Pacifico&family=Gentium+Book+Plus:wght@400;700&family=Open+Sans:wght@400&display=swap">
<style>
  :root {
    --paper: #ffffff;
    --turq-heading: #8dd2d8;
    --turq-text: #7cc3c9;
    --turq-strong: #3fb0bb;
    --turq-mid: #6cc4cc;
    --turq-pale: #a6dce0;
    --turq-line: #c9ebee;
  }
  * { box-sizing: border-box; margin: 0; padding: 0; }
  html, body { width: 1200px; height: 900px; overflow: hidden; background: var(--paper); }
  .panel { position: relative; width: 1200px; height: 900px; }

  .section-title {
    position: absolute;
    font-family: "Pacifico", cursive;
    font-weight: 400;
    font-size: 60px;
    line-height: 1;
    color: var(--turq-heading);
    letter-spacing: -1px;
  }
  .body-copy {
    position: absolute;
    font-family: "Gentium Book Plus", Georgia, serif;
    font-weight: 700;
    font-size: 22px;
    line-height: 42.3px;
    color: var(--turq-text);
    text-align: justify;
    width: 475px;
  }

  .story-title { left: 86px; top: 72px; }
  .story-copy { left: 88px; top: 196px; }
  .signature {
    position: absolute; left: 88px; top: 578px;
    font-family: "Gentium Book Plus", Georgia, serif;
    font-size: 27px; color: var(--turq-text);
  }
  .brand-mark {
    position: absolute; left: 86px; top: 742px;
    display: flex; align-items: center; gap: 10px;
    font-family: "Gentium Book Plus", Georgia, serif;
    font-size: 28px; color: var(--turq-text);
  }
  .brand-mark .dot { width: 18px; height: 18px; border-radius: 50%; background: var(--turq-text); }

  .care-title { left: 630px; top: 72px; }
  .care-copy { left: 633px; top: 197px; }
  .care-icons { position: absolute; left: 633px; top: 382px; display: flex; gap: 8px; }
  .care-icons svg { width: 35px; height: 35px; display: block; }

  .size-title { left: 628px; top: 484px; }
  .size-chart {
    position: absolute; left: 622px; top: 620px;
    display: grid; grid-template-columns: repeat(6, 43px);
    font-family: "Open Sans", Arial, sans-serif; font-size: 11px; color: var(--turq-strong);
  }
  .size-col {
    display: flex; flex-direction: column; align-items: center;
    border-right: 1px dotted var(--turq-line); height: 120px;
  }
  .size-col:last-child { border-right: none; }
  .size-num {
    width: 22px; height: 22px; border-radius: 50%;
    color: #fff; font-size: 15px; line-height: 22px; text-align: center;
  }
  .size-dots { display: flex; gap: 2px; margin-top: 5px; }
  .size-dots i { width: 5px; height: 5px; border-radius: 50%; background: var(--turq-pale); display: block; }
  .size-dots i.on { background: var(--turq-strong); }
  .size-label { margin-top: 14px; }
  .size-range { margin-top: 30px; }
  .tone-strong { background: var(--turq-strong); }
  .tone-mid { background: var(--turq-mid); }
  .tone-pale { background: var(--turq-pale); }
</style>
</head>
<body>
<main class="panel">
  <h2 class="section-title story-title">Our story</h2>
  <p class="body-copy story-copy">Lorem ipsum dolor sit amet, consectetur adipiscing elit. Donec egestas arcu at dolor venenatis, vitae lobortis diam bibendum. Nulla facilisi. Nulla euismod sed augue et aliquam. Sed tempus urna id ligula vehicula facilisis. Aliquam dictum sodales massa. Aenean id urna rhoncus, elementum tortor eget, accumsan nisi.</p>
  <p class="signature">Marla &amp; Jen</p>
  <div class="brand-mark"><span class="dot"></span>Pebble &amp; Co</div>

  <h2 class="section-title care-title">Care instructions</h2>
  <p class="body-copy care-copy">Lorem ipsum dolor sit amet, consectetur adipiscing elit. Donec egestas arcu at dolor venenatis, vitae lobortis diam bibendum. Nulla facilisi.</p>

  <div class="care-icons" aria-label="Care symbols">
    <svg viewBox="0 0 35 35"><rect x="0.5" y="0.5" width="34" height="34" rx="2" fill="none" stroke="#7cc3c9"/><path d="M8 13 L11 25 H24 L27 13" fill="none" stroke="#7cc3c9" stroke-width="1.3"/><path d="M8 15 q3 -2 6 0 t6 0 t6 0" fill="none" stroke="#7cc3c9"/><path d="M15 19 l5 4" stroke="#7cc3c9"/></svg>
    <svg viewBox="0 0 35 35"><rect x="0.5" y="0.5" width="34" height="34" rx="2" fill="none" stroke="#7cc3c9"/><path d="M8 13 L11 25 H24 L27 13" fill="none" stroke="#7cc3c9" stroke-width="1.3"/><path d="M8 15 q3 -2 6 0 t6 0 t6 0" fill="none" stroke="#7cc3c9"/><path d="M15 19 l5 4 M20 19 l-5 4" stroke="#7cc3c9"/></svg>
    <svg viewBox="0 0 35 35"><rect x="0.5" y="0.5" width="34" height="34" rx="2" fill="none" stroke="#7cc3c9"/><rect x="7" y="7" width="21" height="21" fill="none" stroke="#7cc3c9"/><circle cx="17.5" cy="17.5" r="7.5" fill="none" stroke="#7cc3c9"/></svg>
    <svg viewBox="0 0 35 35"><rect x="0.5" y="0.5" width="34" height="34" rx="2" fill="none" stroke="#7cc3c9"/><rect x="7" y="7" width="21" height="21" fill="none" stroke="#7cc3c9"/><circle cx="17.5" cy="17.5" r="8" fill="#3fb0bb"/></svg>
    <svg viewBox="0 0 35 35"><rect x="0.5" y="0.5" width="34" height="34" rx="2" fill="none" stroke="#7cc3c9"/><rect x="7" y="7" width="21" height="21" fill="none" stroke="#7cc3c9"/><circle cx="17.5" cy="17.5" r="7.5" fill="none" stroke="#7cc3c9"/><path d="M7 7 L28 28 M28 7 L7 28" stroke="#7cc3c9"/></svg>
    <svg viewBox="0 0 35 35"><rect x="0.5" y="0.5" width="34" height="34" rx="2" fill="none" stroke="#7cc3c9"/><rect x="7" y="7" width="21" height="21" fill="none" stroke="#7cc3c9"/><circle cx="17.5" cy="17.5" r="7.5" fill="none" stroke="#7cc3c9"/><path d="M11 24 H24" stroke="#7cc3c9"/></svg>
  </div>

  <h2 class="section-title size-title">Size chart</h2>
  <div class="size-chart">
    <div class="size-col"><span class="size-num tone-strong">1</span><span class="size-dots"><i class="on"></i><i></i><i></i><i></i></span><span class="size-label">P</span><span class="size-range">P-XS</span></div>
    <div class="size-col"><span class="size-num tone-pale">2</span><span class="size-dots"><i class="on"></i><i class="on"></i><i></i><i></i></span><span class="size-label">XS</span><span class="size-range">XS-S</span></div>
    <div class="size-col"><span class="size-num tone-pale">3</span><span class="size-dots"><i class="on"></i><i class="on"></i><i class="on"></i><i></i></span><span class="size-label">S</span><span class="size-range">S-M</span></div>
    <div class="size-col"><span class="size-num tone-strong">4</span><span class="size-dots"><i class="on"></i><i class="on"></i><i class="on"></i><i class="on"></i></span><span class="size-label">M</span><span class="size-range">M-L</span></div>
    <div class="size-col"><span class="size-num tone-strong">5</span><span class="size-dots"><i></i><i class="on"></i><i class="on"></i><i class="on"></i></span><span class="size-label">L</span><span class="size-range">L-XL</span></div>
    <div class="size-col"><span class="size-num tone-pale">6</span><span class="size-dots"><i></i><i></i><i class="on"></i><i class="on"></i></span><span class="size-label">XL</span><span class="size-range">XL-1X</span></div>
  </div>
</main>
</body>
</html>
```